Window Company website re-design

We are creating a new website design for http://harborpanes.example and we are going to be using wordpress for the site. The idea is to make it appeal to homeowners, more than half of the visitors will be female so the design must appeal to them with appropriate colors and shapes. Historically the website has been dark with a black background and the idea is to keep some of that but make it much brighter with textures and inviting colors.
Major competitors which we will mimic are the following in order of favorites:
http://www.birchvalleyglass.example/ (this is something we really like because of the full width, call to action, easy to navigate, space for
http://www.grainhillexteriors.example/ (this is a nice wide design with a lot of great image space and call to actions)
http://www.restorebyhollister.example/ (the full width is nice here)
http://www.duskpointpanes.example/ (the slide over option showing the window is nice here.)
Others:
http://www.torvane.example/
http://www.quiro.example/home/default.aspx
http://www.hollisterpanes.example/
https://www.glazeplanet.example/
http://www.delcot.example/

Harbor is the leader in the industry so they want a design that is going to portray that. The owners say that their competitors always copy what they do so this design must be cutting edge.

Important elements need to included:
1. Make the design convey very obviously they are a replacement window and door company.
2. Very clear “request a free estimate” call to action box on the homepage.
3. Area for the “Live Support” call to action
4. Navigation:

- Home
- Why Harbor
o Saves Dollars, Makes Sense
o We Have You Covered Start to Finish
o The Harbor Difference
o Pitfalls to Avoid
- Windows and Doors
o Windows
 Double Hung Windows
 Awning Windows
 Basement Hopper Windows
 Bow Windows
 Garden Windows
 Casement Windows
 Bay Windows
 Slider Windows
 Dead-Lite / Specialty / Transom
o Doors
 Storm Doors
 Harbor French Doors
 Patio Slider Doors
 Door Catalog
 Keypad Deadbolt
o Before and After
- About Us
o Testimonials
o Directions
o Warranty
o Employment
o Manufacturing process
o Home Shows
o Community Involvement
- Financing
- Commercial Division
- Careers
- Contact Us

Important elements for the Home Page:
1. Call to action – request a free quote
2. Awards
3. Live support
4. Guarantee
5. Featured testimonials
6. Press releases
7. Locations (Map?)

The attached photos can be used for the homepage images

Target Market(s)

The target market is middle income home owners who want good quality and great service.

Industry/Entity Type

Industry

Font styles to use
Sans Serif

Colors

Designer to choose colors to be used in the design.

Requirements
Must have
• We will need 2 designs, one for the homepage and the other for the inner pages.

2. Awards
3. Live support
4. Guarantee
5. Featured testimonials
6. Press releases
7. Locations (Map?)

```html
<!DOCTYPE html>
<html lang="en">
<head>
<meta charset="utf-8">
<title>Harbor</title>
<link href="https://fonts.googleapis.com/css2?family=Arimo:wght@400;700&display=swap" rel="stylesheet">
<style>
  :root{
    --page-bg:#efeeea;
    --nav-bg:#050505;
    --nav-link:#9ee07f;
    --room-light:#f2efe6;
    --room-mid:#d9d3c4;
    --floor:#c9a77c;
    --sun:#fff27a;
    --headline:#e08a12;
    --body-text:#3b3a35;
    --cta:#f23a5a;
    --cta-text:#ffffff;
    --teal:#5fd8d0;
    --blue:#62a9ea;
    --orange:#f2a64a;
    --green:#8fe07a;
    --ink:#1f1f1f;
    --support-bg:rgba(240,238,232,.88);
    --support-online:#3aa83a;
    --badge:#b9b3a8;
  }
  *{box-sizing:border-box;margin:0;padding:0}
  html,body{width:1200px;height:1000px;overflow:hidden}
  body{background:var(--page-bg);font-family:"Arimo",Arial,sans-serif;position:relative}

  .site{position:absolute;left:0;top:110px;width:1200px;height:780px;overflow:hidden;background:var(--room-light)}

  .main-nav{position:absolute;left:0;top:0;width:100%;height:45px;background:var(--nav-bg);display:flex;align-items:center;padding-left:90px}
  .main-nav a{color:var(--nav-link);text-decoration:none;font-size:17px;margin-right:32px}
  .search-box{position:absolute;right:12px;top:8px;width:245px;height:29px;background:#fff;border:2px solid #7fc7c0;border-radius:8px}
  .search-box svg{position:absolute;right:10px;top:4px}

  .hero-photo{position:absolute;left:0;top:45px;width:100%;height:735px;
    background:
      linear-gradient(180deg,rgba(0,0,0,0) 62%,var(--floor) 63%,#b88f62 100%),
      radial-gradient(ellipse at 42% 30%,#bfe0f4 0 14%,rgba(191,224,244,0) 24%),
      linear-gradient(90deg,#cfcabd 0%,var(--room-light) 30%,var(--room-mid) 75%,#bdb6a6 100%)}

  .phone-number{position:absolute;left:25px;top:68px;font-size:16px;color:var(--ink)}

  .brand{position:absolute;left:0;width:100%;top:82px;text-align:center}
  .brand-mark{display:inline-block;width:70px;height:70px;background:var(--ink);vertical-align:middle}
  .brand-name{display:block;font-size:52px;font-weight:700;color:var(--ink);margin-top:8px;line-height:1}

  .warranty-badge{position:absolute;left:1018px;top:60px;width:150px;height:150px;border-radius:50%;background:var(--badge);opacity:.8}

  .sun-circle{position:absolute;left:-5px;top:268px;width:390px;height:390px;border-radius:50%;background:var(--sun);opacity:.72}
  .hero-copy{position:absolute;left:42px;top:400px;width:320px}
  .hero-copy h1{font-size:31px;font-weight:400;color:var(--headline);line-height:1.3;letter-spacing:.5px}
  .hero-copy p{font-size:14px;color:var(--body-text);line-height:1.35;margin-top:12px}

  .slide-arrow{position:absolute;top:320px;width:60px;height:60px;border-radius:50%;background:rgba(120,120,120,.35)}
  .slide-arrow.prev{left:5px}
  .slide-arrow.next{left:1122px}
  .slide-arrow svg{position:absolute;left:20px;top:18px}

  .quote-button{position:absolute;left:633px;top:418px;width:345px;height:70px;border-radius:12px;background:var(--cta);color:var(--cta-text);font-size:22px;display:flex;align-items:center;justify-content:center;letter-spacing:.5px}

  .quick-links{position:absolute;left:0;top:620px;width:600px;height:160px}
  .quick-link{position:absolute;width:110px;text-align:center}
  .quick-link .icon{width:110px;height:110px;border-radius:50%;display:flex;align-items:center;justify-content:center}
  .quick-link span{display:block;font-size:14px;color:var(--ink);margin-top:6px;line-height:1.2}
  .icon.teal{background:var(--teal)}
  .icon.blue{background:var(--blue)}
  .icon.orange{background:var(--orange)}
  .icon.green{background:var(--green)}
  .icon .question{font-size:62px;color:#16355a;font-weight:400;margin-top:0}

  .live-support{position:absolute;left:983px;top:648px;width:190px;height:85px;border-radius:12px;background:var(--support-bg);text-align:center;padding-top:22px}
  .live-support .label{font-size:12px;color:var(--ink);letter-spacing:.3px}
  .live-support .status{font-size:17px;color:var(--support-online);margin-top:4px}
</style>
</head>
<body>
  <main class="site">
    <div class="hero-photo" role="img" aria-label="Bright empty room with large windows and light wood floor"></div>

    <nav class="main-nav">
      <a href="#">About</a>
      <a href="#">Windows &amp; Doors</a>
      <a href="#">Why us?</a>
      <a href="#">Request free quote</a>
      <a href="#">Financing</a>
      <a href="#">Contact</a>
      <div class="search-box">
        <svg width="20" height="20" viewBox="0 0 20 20"><circle cx="8" cy="8" r="5.5" fill="none" stroke="#111" stroke-width="2.5"/><line x1="12" y1="12" x2="18" y2="18" stroke="#111" stroke-width="3"/></svg>
      </div>
    </nav>

    <div class="phone-number">1-800-555-0142</div>

    <div class="brand">
      <span class="brand-mark"></span>
      <span class="brand-name">Harbor</span>
    </div>

    <div class="warranty-badge" role="img" aria-label="Lifetime warranty seal"></div>

    <div class="sun-circle"></div>
    <div class="slide-arrow prev"><svg width="20" height="24" viewBox="0 0 20 24"><path d="M15 2 L4 12 L15 22" fill="none" stroke="#fff" stroke-width="4"/></svg></div>
    <div class="slide-arrow next"><svg width="20" height="24" viewBox="0 0 20 24"><path d="M5 2 L16 12 L5 22" fill="none" stroke="#fff" stroke-width="4"/></svg></div>

    <section class="hero-copy">
      <h1>LET THE LIGHT<br>SHINE IN!</h1>
      <p>Welcome to Harbor Windows.<br>Find the perfect window or door for<br>your needs. Get help with financing and<br>installation. Request a free quote today.</p>
    </section>

    <a class="quote-button">REQUEST FREE QUOTE</a>

    <section class="quick-links">
      <div class="quick-link" style="left:60px">
        <div class="icon teal">
          <svg width="52" height="66" viewBox="0 0 52 66"><path d="M4 64 V24 A22 22 0 0 1 48 24 V64 Z" fill="none" stroke="#14514c" stroke-width="5"/><line x1="26" y1="4" x2="26" y2="64" stroke="#14514c" stroke-width="5"/><line x1="4" y1="36" x2="48" y2="36" stroke="#14514c" stroke-width="5"/></svg>
        </div>
        <span>Find Windows and Doors</span>
      </div>
      <div class="quick-link" style="left:188px">
        <div class="icon blue"><span class="question">?</span></div>
        <span>Why us?</span>
      </div>
      <div class="quick-link" style="left:318px">
        <div class="icon orange" role="img" aria-label="Map of office locations"></div>
        <span>Locate nearest office</span>
      </div>
      <div class="quick-link" style="left:448px">
        <div class="icon green">
          <svg width="44" height="60" viewBox="0 0 44 60"><rect x="2" y="2" width="40" height="56" rx="3" fill="none" stroke="#2c5a22" stroke-width="4"/><rect x="8" y="8" width="28" height="10" fill="#2c5a22"/><g fill="#2c5a22"><rect x="8" y="24" width="7" height="6"/><rect x="18" y="24" width="7" height="6"/><rect x="28" y="24" width="7" height="6"/><rect x="8" y="34" width="7" height="6"/><rect x="18" y="34" width="7" height="6"/><rect x="28" y="34" width="7" height="6"/><rect x="8" y="44" width="7" height="6"/><rect x="18" y="44" width="7" height="6"/><rect x="28" y="44" width="7" height="6"/></g></svg>
        </div>
        <span>Get help financing</span>
      </div>
    </section>

    <aside class="live-support">
      <div class="label">GET LIVE SUPPORT</div>
      <div class="status">ONLINE</div>
    </aside>
  </main>
</body>
</html>
```